Physiotherapy Referral Pad

-Need a referral pad for physiotherapy to be provided to doctors' offices. I would like it to be simple, not too cluttered and sharp looking so doctors can quickly complete it for clients.

-I have attached my logo which I would like to include. I have also included my business cards to keep the style, font, colors etc consistent.

-I would like to include my slogan
From Our Home To Yours

-I would like it to include services options with tick boxes for Mobile, Clinic, Telehealth, KTOQFE

-I would like for it to say Call to Book or Book Online

-I would like it to include my clinic address:
427 Marden Lane
Whitehorse, YT
Y0B2K9

-I would like it to include my contact info:
Cole Pratt BSc(kin), MPT, CAFCI, IMS
(867)555-0142
physio@quarnetherapy.example

-I would like lines for the following:
Patient Name:
Diagnosis/Recommendations:
(extra lines to fill out patient info)

Physician Signature
Date

Target Market(s)

Physicians to refer clients to physiotherapy

Industry/Entity Type

Physical Therapy

Requirements
Must have
• Clean, concise, easy to look at and find pertinant categories for physicians
Nice to have
• Quarne Therapy color scheme. Please see business cards and website as needed
Should not have
• Not too cluttered or wordy

```html
<!DOCTYPE html>
<html lang="en">
<head>
<meta charset="utf-8">
<title>Quarne Therapy – Referral Pad</title>
<link rel="stylesheet" href="https://fonts.googleapis.com/css2?family=Playfair+Display:wght@700;900&family=Poppins:wght@400;500;600&display=swap">
<style>
  :root {
    --navy: #2c4670;
    --navy-deep: #1e3358;
    --teal: #14a086;
    --blue: #1a88bf;
    --ink: #222a38;
    --rule: #9aa1ab;
    --paper: #ffffff;
    --backdrop: #e9e5e1;
  }
  * { box-sizing: border-box; margin: 0; padding: 0; }
  html, body { width: 1200px; height: 1088px; overflow: hidden; }
  body {
    background: var(--backdrop);
    font-family: "Poppins", sans-serif;
    color: var(--ink);
    position: relative;
  }
  .referral-pad {
    position: absolute;
    left: 200px; top: 24px;
    width: 800px; height: 1040px;
    background: var(--paper);
    box-shadow: 0 6px 24px rgba(0,0,0,0.12);
    overflow: hidden;
  }
  .brand {
    position: absolute; top: 62px; left: 0; width: 100%;
    display: flex; justify-content: center; align-items: center; gap: 12px;
  }
  .brand-mark { width: 18px; height: 18px; background: var(--navy); }
  .brand-name {
    font-family: "Playfair Display", serif; font-weight: 900;
    font-size: 38px; letter-spacing: 3px; color: var(--navy);
    text-transform: uppercase;
  }
  .contact-band {
    position: absolute; top: 196px; left: 22px; right: 0; height: 76px;
    display: flex;
  }
  .book-online {
    width: 204px; background: var(--teal); color: #fff;
    font-weight: 600; font-size: 20px; letter-spacing: 0.5px;
    display: flex; align-items: center; justify-content: center;
  }
  .practitioner {
    width: 180px; margin-left: 4px; background: var(--navy); color: #fff;
    display: flex; flex-direction: column; align-items: center; justify-content: center;
  }
  .practitioner-name { font-family: "Playfair Display", serif; font-weight: 700; font-size: 26px; line-height: 1.1; }
  .practitioner-creds { font-size: 9px; margin-top: 3px; }
  .contact-info {
    flex: 1; margin-left: 4px; background: var(--blue); color: #fff;
    display: flex; flex-direction: column; justify-content: center;
    padding-left: 16px; font-size: 12px; line-height: 1.9; white-space: nowrap;
  }
  .contact-info b { font-weight: 600; }
  .slogan {
    position: absolute; top: 316px; left: 0; width: 100%; text-align: center;
    font-family: "Playfair Display", serif; font-weight: 900;
    font-size: 27px; color: var(--navy-deep); letter-spacing: 1px;
  }
  .form { position: absolute; top: 380px; left: 84px; right: 60px; }
  .field { display: flex; align-items: flex-end; height: 34px; font-size: 13px; }
  .field-label { white-space: nowrap; padding-right: 6px; }
  .fill { flex: 1; border-bottom: 1px dashed var(--rule); height: 1px; margin-bottom: 4px; }
  .field-pair { display: flex; gap: 16px; }
  .field-pair .field:first-child { flex: 1.9; }
  .field-pair .field:last-child { flex: 1; }
  .field-pair.right-only { justify-content: flex-end; }
  .field-pair.right-only .field { flex: 0 0 250px; }
  .section-title { color: var(--navy); font-weight: 600; font-size: 15px; }
  .procedures { margin-top: 32px; }
  .options { display: flex; gap: 22px; margin-top: 12px; font-size: 13px; }
  .option { display: flex; align-items: center; gap: 9px; }
  .tick-box { width: 15px; height: 15px; border: 1.5px solid var(--ink); }
  .diagnosis { margin-top: 28px; }
  .signoff { margin-top: 18px; }
  .signoff .field-label { color: var(--navy); font-weight: 600; font-size: 14px; }
  .site-footer {
    position: absolute; left: 0; right: 0; bottom: 0; height: 62px;
    background: var(--navy); color: #fff;
    display: flex; align-items: center; justify-content: center;
    font-size: 13px; letter-spacing: 5px; text-transform: uppercase;
  }
</style>
</head>
<body>
  <main class="referral-pad">
    <header class="brand">
      <span class="brand-mark"></span>
      <span class="brand-name">Quarne Therapy</span>
    </header>

    <section class="contact-band">
      <div class="book-online">BOOK ONLINE</div>
      <div class="practitioner">
        <span class="practitioner-name">Cole Pratt</span>
        <span class="practitioner-creds">BSc(kin), MPT, CAFCI, IMS</span>
      </div>
      <div class="contact-info">
        <span><b>P:</b> (867)555-0142 &nbsp;<b>E:</b> physio@quarnetherapy.example</span>
        <span><b>A:</b> 427 Marden Lane, Whitehorse, YT Y0B2K9</span>
      </div>
    </section>

    <h1 class="slogan">FROM OUR HOME TO YOURS</h1>

    <section class="form">
      <div class="field-pair right-only">
        <div class="field"><span class="field-label">Patient Phone #:</span><span class="fill"></span></div>
      </div>
      <div class="field-pair">
        <div class="field"><span class="field-label">Patient Name:</span><span class="fill"></span></div>
        <div class="field"><span class="field-label">Date:</span><span class="fill"></span></div>
      </div>
      <div class="field"><span class="field-label">Patient Email:</span><span class="fill"></span></div>
      <div class="field"><span class="field-label">Patient Address:</span><span class="fill"></span></div>
      <div class="field"><span class="fill"></span></div>
      <div class="field"><span class="fill"></span></div>

      <div class="procedures">
        <h2 class="section-title">Treatment Procedures</h2>
        <div class="options">
          <label class="option"><span class="tick-box"></span>Mobile</label>
          <label class="option"><span class="tick-box"></span>Clinic</label>
          <label class="option"><span class="tick-box"></span>Telehealth</label>
          <label class="option"><span class="tick-box"></span>KTOQFE</label>
        </div>
      </div>

      <div class="diagnosis">
        <div class="field"><span class="field-label section-title">Diagnosis/Recommendations</span><span class="fill"></span></div>
        <div class="field"><span class="fill"></span></div>
        <div class="field"><span class="fill"></span></div>
        <div class="field"><span class="fill"></span></div>
      </div>

      <div class="signoff">
        <div class="field"><span class="field-label">Physician Name:</span><span class="fill"></span></div>
        <div class="field"><span class="field-label">Signature:</span><span class="fill"></span></div>
      </div>
    </section>

    <footer class="site-footer">www.quarnetherapy.example</footer>
  </main>
</body>
</html>
```